Business Card for a Wedding Films Business

We require a business card design for our business 'Lewis Marrow Wedding Films'. The logo needs to look classy and high end.

Target Market(s)

Wedding Couples

Contact Information for Business Card

Lewis Marrow Wedding Films
07312 605 227
films@lewismarrowreels.com
www.lewismarrowreels.com

Facebook: @lewismarrowweddingfilms
Instagram: @lewismarrowfilms

Font styles to use
Sans Serif

Requirements
Must have
• Social media icons - Facebook and Instagram

```html
<!DOCTYPE html>
<html lang="en">
<head>
<meta charset="UTF-8">
<title>Lewis Marrow Wedding Films – Business Card</title>
<link rel="stylesheet" href="https://fonts.googleapis.com/css2?family=Nunito+Sans:wght@300;400&display=swap">
<style>
  :root {
    --backdrop: #cccccc;
    --card: #f7f7f7;
    --ink: #111111;
    --logo-tone: #d9d9d9;
    --card-shadow: rgba(0, 0, 0, 0.18);
  }
  * { margin: 0; padding: 0; box-sizing: border-box; }
  html, body {
    width: 1200px;
    height: 900px;
    overflow: hidden;
    background: var(--backdrop);
    font-family: "Nunito Sans", sans-serif;
  }
  .stage {
    position: relative;
    width: 1200px;
    height: 900px;
  }
  .card {
    position: absolute;
    width: 460px;
    height: 290px;
    background: var(--card);
    box-shadow: 0 14px 30px var(--card-shadow);
    display: flex;
    flex-direction: column;
    align-items: center;
    justify-content: center;
    text-align: center;
  }
  .card--front { left: 300px; top: 150px; }
  .card--back  { left: 460px; top: 470px; }

  .brand-name {
    color: var(--logo-tone);
    font-weight: 300;
    text-transform: uppercase;
    line-height: 1.5;
  }
  .brand-name__main {
    display: block;
    font-size: 22px;
    letter-spacing: 0.32em;
  }
  .brand-name__sub {
    display: block;
    font-size: 10px;
    letter-spacing: 0.6em;
  }

  .contact {
    color: var(--ink);
    font-weight: 400;
  }
  .contact__phone {
    font-size: 17px;
    letter-spacing: 0.02em;
    margin-bottom: 10px;
  }
  .contact__line {
    font-size: 11px;
    line-height: 1.45;
  }
  .social {
    margin-top: 16px;
    display: flex;
    flex-direction: column;
    align-items: center;
    gap: 8px;
  }
  .social__item {
    display: flex;
    flex-direction: column;
    align-items: center;
    gap: 3px;
    font-size: 11px;
  }
  .social__marker {
    width: 13px;
    height: 13px;
    background: var(--ink);
  }
</style>
</head>
<body>
  <main class="stage">
    <section class="card card--front" aria-label="Card front">
      <h1 class="brand-name">
        <span class="brand-name__main">Lewis Marrow</span>
        <span class="brand-name__sub">Wedding Films</span>
      </h1>
    </section>

    <section class="card card--back" aria-label="Card back">
      <div class="contact">
        <p class="contact__phone">07312 605 227</p>
        <p class="contact__line">films@lewismarrowreels.com</p>
        <p class="contact__line">www.lewismarrowreels.com</p>
        <div class="social">
          <div class="social__item">
            <span class="social__marker" aria-hidden="true"></span>
            <span>@lewismarrowweddingfilms</span>
          </div>
          <div class="social__item">
            <span class="social__marker" aria-hidden="true"></span>
            <span>@lewismarrowfilms</span>
          </div>
        </div>
      </div>
    </section>
  </main>
</body>
</html>
```